Fairway Circuit web site

Fairway Circuit is a High End golf amateur Tour targeted to wealthy golf passionates.
The concept is to take average golfers and offer them the same playing conditions than the pros (Caddies, branded bags, TV coverage...) and bring them to the most beautiful golf courses around the world.
Keywords: International, Exclusive, Luxury, but not show-off...
The Task is to design the WordPress template and a exemple page.
Please use the provided logo and any stock image you like.
Updates

Hello,

please note that the outcome has to be a fully coded WordPress site.

Please no "Photoshop only" designs...

Thanks

```html
<!DOCTYPE html>
<html lang="en">
<head>
<meta charset="utf-8">
<title>Fairway Circuit</title>
<link href="https://fonts.googleapis.com/css2?family=Open+Sans:ital,wght@0,400;0,600;0,700;1,400&display=swap" rel="stylesheet">
<style>
:root{
  --page:#175a3c;
  --page-dark:#124a31;
  --band:#217a53;
  --band-light:#2b9467;
  --panel:#1f6e4b;
  --field:#1d6645;
  --footer-bar:#10432c;
  --beige-1:#f3e5c6;
  --beige-2:#c9a774;
  --nav-text:#2f5b3e;
  --white:#ffffff;
  --muted:#cfe3d7;
  --accent:#e3a72b;
  --heading-green:#45b074;
}
*{box-sizing:border-box;margin:0;padding:0}
html,body{width:958px;height:1200px;overflow:hidden}
body{font-family:"Open Sans",Arial,sans-serif;background:var(--page);color:var(--white);position:relative}
.abs{position:absolute}

/* header */
.navbar{left:79px;top:45px;width:799px;height:36px;background:linear-gradient(var(--beige-1),var(--beige-2));}
.nav{left:219px;top:52px;display:flex;gap:30px;font-size:13.5px;color:var(--nav-text);list-style:none}
.search{left:726px;top:50px;width:142px;height:25px;background:var(--page);border-radius:2px;font-size:11px;font-style:italic;color:#e6efe9;padding:5px 12px}
.search svg{position:absolute;right:9px;top:5px}
.brand{left:96px;top:14px;width:88px;height:88px;border-radius:50%;background:var(--page);border:3px solid var(--beige-1);display:flex;align-items:center;justify-content:center;text-align:center;font-size:12px;font-weight:700;line-height:1.15;color:var(--beige-1)}

/* hero */
.hero{left:79px;top:81px;width:799px;height:343px;background:linear-gradient(180deg,#2c2a14 0%,#6b5a23 22%,#4f7a24 45%,#3f7a22 70%,#2d5a18 100%)}
.hero-text{left:337px;top:172px;width:520px;font-weight:700;font-size:19.5px;line-height:24px;text-shadow:0 1px 3px rgba(0,0,0,.5)}
.hero-text .sub{font-weight:400;font-size:13.5px;line-height:20px;display:block;margin:1px 0 2px}
.dots{left:101px;top:388px;display:flex;gap:6px}
.dots span{width:11px;height:11px;border-radius:50%;background:#c9a774}
.dots span.on{background:#fff}
.social{left:840px;top:312px;display:flex;flex-direction:column;gap:6px}
.social span{width:28px;height:28px;border-radius:50%;background:#2f7ac0;font-size:7px;font-weight:600;display:flex;align-items:center;justify-content:center}
.social span.reel{background:#b8302c}
.social span.folk{background:#3a5aa0}

/* content */
.content{left:0;top:424px;width:958px;height:414px;background:radial-gradient(ellipse at 35% 20%,var(--band-light) 0%,var(--band) 45%,var(--page) 100%)}
h2{position:absolute;font-size:20px;font-weight:700}
.welcome{left:97px;top:475px;width:444px;font-size:10.5px;line-height:14.4px;color:#eef5f0}
.readmore{left:486px;top:525px;font-size:10.5px;color:var(--accent)}
.video{left:99px;top:581px;width:450px;height:239px;background:linear-gradient(180deg,#3d5a4a 0%,#4e7a45 40%,#3f6e33 100%)}
.video svg{position:absolute;left:0;top:0}
.news{left:576px;top:474px;width:300px}
.news-item{display:flex;gap:10px;height:81px}
.thumb{width:80px;height:70px;flex:none}
.t1{background:linear-gradient(160deg,#cfd8cf,#4e7d3a)}
.t2{background:linear-gradient(180deg,#6a7a8a,#e2a04a 65%,#3a2e1a)}
.t3{background:linear-gradient(180deg,#5b8fc7,#8fbf5a 60%,#3f7a22)}
.news-text{font-size:10.5px;line-height:14.4px;color:#eef5f0;padding-top:2px}
.news-text .date{display:block;color:var(--accent);margin-top:4px}
.feature{left:576px;width:302px;background:linear-gradient(90deg,var(--panel),rgba(31,110,75,.4));font-size:14px;font-weight:700;display:flex;align-items:center;padding-left:16px;gap:8px}
.feature i{width:11px;height:7px;background:radial-gradient(circle,#6fb08a 40%,transparent 45%) 0 0/3.6px 3.5px}

/* partners */
.partners{left:0;top:838px;width:958px;height:96px;background:radial-gradient(ellipse at 50% 50%,#1f7650 0%,var(--page) 80%);display:flex;align-items:center;justify-content:space-between;padding:0 110px 0 108px;font-size:19px;font-weight:700}

/* footer */
.foot-head{font-size:14.5px;font-weight:600;color:var(--heading-green);top:955px}
.links{left:110px;top:985px;list-style:none;font-size:11.5px;line-height:24px}
.field{left:272px;width:182px;background:var(--field);font-size:10px;font-style:italic;color:#9fc0ad;padding:8px 10px}
.submit{left:273px;top:1121px;width:87px;height:26px;border-radius:2px;background:linear-gradient(var(--beige-1),var(--beige-2));color:var(--nav-text);font-weight:700;font-size:12.5px;display:flex;align-items:center;justify-content:center}
.map{left:544px;top:976px;width:288px;height:160px;background:radial-gradient(ellipse,rgba(0,0,0,.12),transparent 70%)}
.address{left:488px;top:985px;font-size:11.5px;font-style:italic;line-height:24px}
.bottom{left:0;top:1166px;width:958px;height:34px;background:var(--footer-bar)}
.copy{left:670px;top:1174px;font-size:10px;font-style:italic;color:#d6e4db}
</style>
</head>
<body>
  <div class="abs navbar"></div>
  <ul class="abs nav"><li>Home</li><li>Tour</li><li>Tournaments</li><li>Players</li><li>Video</li><li>Contact Us</li></ul>
  <div class="abs search">Search
    <svg width="15" height="15" viewBox="0 0 15 15"><circle cx="6.5" cy="6.5" r="5" fill="none" stroke="#cfe3d7" stroke-width="1.5"/><line x1="10" y1="10" x2="14" y2="14" stroke="#cfe3d7" stroke-width="1.5"/></svg>
  </div>

  <div class="abs hero" role="img" aria-label="Golf ball resting near the hole on a sunlit green"></div>
  <div class="abs brand">Fairway<br>Circuit</div>
  <p class="abs hero-text">Our idea is to take average golfers and offer them the same playing conditions than the pros
    <span class="sub">(Caddies, branded bags, TV coverage...)</span>
    and bring them to the most beautiful golf courses around the world</p>
  <div class="abs dots"><span></span><span></span><span class="on"></span></div>
  <div class="abs social"><span>Chirp</span><span class="reel">Reel</span><span class="folk">Folk</span></div>

  <div class="abs content"></div>
  <h2 style="left:97px;top:432px">Welcome</h2>
  <p class="abs welcome">Nam libero tempore, cum soluta nobis est eligendi optio cumque nihil impedit quo minus id quod maxime placeat facere possimus, omnis voluptas assumenda est, omnis dolor repel-lendus. Temporibus autem quibusdam et aut officiis debitis aut rerum necessitatibus saepe eveniet ut et voluptates</p>
  <span class="abs readmore">Readmore</span>
  <h2 style="left:97px;top:540px">Video</h2>
  <div class="abs video" role="img" aria-label="Video still of a golfer crouching to read a putt">
    <svg width="450" height="239" viewBox="0 0 450 239">
      <circle cx="217" cy="113" r="34" fill="none" stroke="rgba(255,255,255,.75)" stroke-width="3"/>
      <polygon points="208,97 208,129 232,113" fill="rgba(255,255,255,.75)"/>
      <rect x="9" y="223" width="402" height="3" fill="rgba(255,255,255,.4)"/>
      <rect x="420" y="220" width="2" height="8" fill="rgba(255,255,255,.7)"/>
      <rect x="424" y="220" width="2" height="8" fill="rgba(255,255,255,.7)"/>
      <polygon points="433,220 433,228 438,224" fill="rgba(255,255,255,.7)"/>
    </svg>
  </div>

  <h2 style="left:574px;top:432px">Recent News</h2>
  <div class="abs news">
    <div class="news-item"><div class="thumb t1" role="img" aria-label="Gloved hand placing a ball on a tee"></div><p class="news-text">Nam libero tempore, cum soluta nobis est eligendi optio cumque nihil impedit quo minus id quod<span class="date">18-02-2014</span></p></div>
    <div class="news-item"><div class="thumb t2" role="img" aria-label="Golfers silhouetted against a sunset"></div><p class="news-text">Nam libero tempore, cum soluta nobis est eligendi optio cumque nihil impedit quo minus id quod<span class="date">18-02-2014</span></p></div>
    <div class="news-item"><div class="thumb t3" role="img" aria-label="Driver lined up behind a teed ball"></div><p class="news-text">Nam libero tempore, cum soluta nobis est eligendi optio cumque nihil impedit quo minus id quod<span class="date">18-02-2014</span></p></div>
  </div>
  <div class="abs feature" style="top:711px;height:38px"><i></i>Caddies</div>
  <div class="abs feature" style="top:751px;height:40px"><i></i>Branded Bags</div>
  <div class="abs feature" style="top:793px;height:45px"><i></i>TV Coverage</div>

  <div class="abs partners"><span>Northway Rentals</span><span>stillframe</span><span>Kestrel</span><span>Harrow Lager</span><span>Metrix</span><span>Velora</span></div>

  <h3 class="abs foot-head" style="left:107px">Quick Links</h3>
  <h3 class="abs foot-head" style="left:268px">Contact Us</h3>
  <h3 class="abs foot-head" style="left:483px">Location</h3>
  <ul class="abs links"><li>Home</li><li>About Us</li><li>Tour</li><li>Tournaments</li><li>Players</li><li>Video</li><li>Contact Us</li></ul>
  <div class="abs field" style="top:986px;height:30px">Name</div>
  <div class="abs field" style="top:1019px;height:29px">Email</div>
  <div class="abs field" style="top:1051px;height:66px">Message</div>
  <div class="abs submit">Submit</div>
  <div class="abs map" role="img" aria-label="Faint world map with location pins"></div>
  <p class="abs address">#14, Links Row,<br>Greenhill,<br>Cityname.<br>Country.<br>Fax : 410 33817<br>Phone : 0800 112 904</p>
  <div class="abs bottom"></div>
  <p class="abs copy">© 2014.www.fairwaycircuit.example</p>
</body>
</html>
```